Letterhead for NZ School promoting centennial celebrations

Our local Primary School (grade school) is turning 100 in 2014 and we would like the letterhead to be updated and incorporate the words "Celebrating 100yrs in 2014" to start creating a bit of interest.
The schools name is Waikora, which is Maori for 'the stitchbird'. The school is quintessential rural new zealand, but very close to Auckland city and is well patronised. The colours of the school are white, maroon and yellow, but predominantly maroon. The emblem/logo is on the existing letterhead and will need some work as it is of rather poor quality. It is of the Hihi (stitchbird) perched on a Kowhai branch. The winning design could lead to work in further updating of the emblem.
We would like the letterhead to be modernised, but not to the point where you wouldn't think it was for a rural nz school, if that makes sense!
Updates

Thanks for all your ideas so far. A couple of pointers: the footer space would be best left empty as we may use this area to put sponsors names - If you are using a watermark would prefer just the bird and no extra colour with it - The ones that are standing out at the moment are flowy (?) modern, not too clunky, busy or boxy. Thanks again.

Forgot to mention we would also now like the dates for the event on there which are
7-9 March
Thanks, Gerald.

Industry/Entity Type

School

Requirements
Must have
• Waikora Primary School
'Celebrating 100yrs in 2014'
school motto: CHARACTER – KINDNESS – COURTESY
TELEPHONE 09-418-5532
FAX 09-418-5539
office@waikora-example.school.nz
and must have the school emblem
Should not have
• Not too much background colour, as I believe the school prints it's own paper. But this is really only a guideline, if it looks good I'm flexible.
I don't think it should have colours other than maroon, white, yellow and black, but realising that is fairly rough palette will be open to a splash of something else if it works better.
The writing below the bird could be removed also.

```html
<!DOCTYPE html>
<html lang="en">
<head>
<meta charset="utf-8">
<title>Waikora Primary School – Letterhead Options</title>
<link rel="stylesheet" href="https://fonts.googleapis.com/css2?family=Tinos:ital,wght@1,700&family=Source+Sans+3:wght@400;700&display=swap">
<style>
  :root {
    --maroon: #7b2a2c;
    --board: #a8832b;
    --paper: #ffffff;
    --ink: #3a3a3a;
    --rule: #c9c2c2;
    --watermark: #f1efef;
    --emblem-tint: #f6eeee;
  }
  * { margin: 0; padding: 0; box-sizing: border-box; }
  html, body {
    width: 1200px; height: 760px; overflow: hidden;
    background: var(--board);
  }
  .board { position: relative; width: 1200px; height: 760px; }

  .sheet {
    position: absolute; top: 42px;
    width: 517px; height: 668px;
    background: var(--paper);
    box-shadow: 2px 3px 4px rgba(0,0,0,0.45);
    overflow: hidden;
  }
  .sheet--footer { left: 56px; }
  .sheet--header { left: 604px; }

  /* Emblem stand-in */
  .emblem {
    position: absolute;
    width: 130px; height: 108px;
    display: flex; align-items: center; justify-content: center; gap: 6px;
    background: var(--emblem-tint);
  }
  .emblem__mark {
    width: 10px; height: 10px; border-radius: 50%;
    background: var(--maroon);
  }
  .emblem__name {
    font-family: "Source Sans 3", sans-serif;
    font-weight: 700; font-size: 18px;
    color: var(--maroon);
  }

  .divider {
    position: absolute; width: 1px; background: var(--rule);
  }

  .school-name {
    position: absolute;
    font-family: "Tinos", "Times New Roman", serif;
    font-style: italic; font-weight: 700;
    font-size: 17px; color: var(--maroon);
    white-space: nowrap;
  }
  .centennial {
    position: absolute;
    font-family: "Source Sans 3", sans-serif;
    font-weight: 700; font-size: 11px;
    color: var(--maroon); white-space: nowrap;
  }
  .motto {
    position: absolute;
    font-family: "Source Sans 3", sans-serif;
    font-weight: 700; color: var(--maroon);
    white-space: nowrap;
  }
  .contact {
    position: absolute;
    font-family: "Source Sans 3", sans-serif;
    font-size: 8px; color: var(--ink);
    white-space: nowrap;
  }
  .contact b { color: var(--maroon); font-weight: 700; }
  .contact span + span { margin-left: 14px; }

  .watermark {
    position: absolute;
    width: 300px; height: 300px;
    display: flex; align-items: center; justify-content: center;
    font-family: "Source Sans 3", sans-serif;
    font-weight: 700; font-size: 62px;
    color: var(--watermark);
  }

  /* Sheet 1: footer contact layout */
  .sheet--footer .emblem { left: 104px; top: 18px; }
  .sheet--footer .divider { left: 250px; top: 43px; height: 43px; }
  .sheet--footer .school-name { left: 269px; top: 44px; }
  .sheet--footer .centennial { left: 284px; top: 69px; }
  .sheet--footer .watermark { left: 214px; top: 248px; }
  .sheet--footer .motto {
    left: 0; width: 100%; top: 627px;
    text-align: center; font-size: 12px;
  }
  .sheet--footer .contact {
    left: 0; width: 100%; top: 645px; text-align: center;
  }
  .sheet--footer .contact span + span { margin-left: 14px; }
  .sheet--footer .contact .email { margin-left: 20px; }

  /* Sheet 2: header contact layout */
  .sheet--header .emblem { left: 102px; top: 18px; }
  .sheet--header .divider { left: 248px; top: 33px; height: 76px; }
  .sheet--header .school-name { left: 264px; top: 28px; }
  .sheet--header .centennial { left: 264px; top: 51px; }
  .sheet--header .motto { left: 264px; top: 77px; font-size: 10px; }
  .sheet--header .contact.phone-line { left: 264px; top: 95px; }
  .sheet--header .contact.email-line { left: 264px; top: 107px; }
  .sheet--header .watermark { left: -100px; top: 243px; }
</style>
</head>
<body>
<main class="board">

  <section class="sheet sheet--footer" aria-label="Letterhead with contact footer">
    <div class="emblem" role="img" aria-label="School emblem: stitchbird perched on a kowhai branch">
      <span class="emblem__mark"></span><span class="emblem__name">Waikora</span>
    </div>
    <div class="divider"></div>
    <h1 class="school-name">Waikora Primary School</h1>
    <p class="centennial">'Celebrating 100yrs in 2014'</p>
    <div class="watermark" role="img" aria-label="Faint emblem watermark">Waikora</div>
    <p class="motto">CHARACTER – KINDNESS – COURTESY</p>
    <p class="contact">
      <span><b>TELEPHONE</b> : 09-418-5532</span>
      <span><b>FAX</b> : 09-418-5539</span>
      <span class="email">office@waikora-example.school.nz</span>
    </p>
  </section>

  <section class="sheet sheet--header" aria-label="Letterhead with contact header">
    <div class="emblem" role="img" aria-label="School emblem: stitchbird perched on a kowhai branch">
      <span class="emblem__mark"></span><span class="emblem__name">Waikora</span>
    </div>
    <div class="divider"></div>
    <h1 class="school-name">Waikora Primary School</h1>
    <p class="centennial">'Celebrating 100yrs in 2014'</p>
    <p class="motto">CHARACTER – KINDNESS – COURTESY</p>
    <p class="contact phone-line">
      <span><b>TELEPHONE</b> : 09-418-5532</span>
      <span><b>FAX</b> : 09-418-5539</span>
    </p>
    <p class="contact email-line">office@waikora-example.school.nz</p>
    <div class="watermark" role="img" aria-label="Faint emblem watermark">Waikora</div>
  </section>

</main>
</body>
</html>
```